Selling my Home Flyer

I need a flyer/brochure for a house listing I am putting together. I will put all of the information together for you to include in the flyer. This will only be a front and back flyer. No extra pages and no staples will be seen. This will be printed by a large office copier, not a professional copier on standard paper. Therefore no crazy dark backgrounds with lots of bleeding colors. Pictures that I want need for sure in there are Aerial with outline, Front from left, and one of the ones showing the large yard. I included a couple sample designs that I don't hate. But feel free to get creative. I will need this on a quick turnaround and I will make comments quickly as well, so submit ASAP.

Target Market(s)

People that will by my house.

Industry/Entity Type

Real Estate Agent

Font styles to use
Serif
Sans Serif

Colors

Designer to choose colors to be used in the design.

Requirements
Must have
• The pictures I mentioned above. And the price and SF and address! I forgot to tell you the address. It is 4817 Heron Lane, Palm Beach Gardens, FL 58127.
Should not have
• Anarchy. I don't want it to look too crazy. Should be pretty straight forward.

```html
<!DOCTYPE html>
<html lang="en">
<head>
<meta charset="utf-8">
<title>Pool Home Listing Flyer – Front and Back</title>
<link rel="stylesheet" href="https://fonts.googleapis.com/css2?family=Oswald:wght@400;500&family=Montserrat:wght@500;600&family=Open+Sans:wght@400;600&display=swap">
<style>
  :root{
    --paper:#ffffff;
    --backdrop:#e6e6e4;
    --gold:#9a8052;
    --ink:#2e2e2e;
    --band-dark:#353535;
    --footer:#5b5b5b;
    --on-dark:#ffffff;
    --photo-green:#5f8a4a;
    --photo-sky:#8fb7d6;
    --photo-roof:#b9765a;
    --photo-interior:#d9cbb6;
  }
  *{box-sizing:border-box;margin:0;padding:0}
  html,body{width:1200px;height:1200px;overflow:hidden}
  body{background:var(--backdrop);font-family:"Open Sans",Arial,sans-serif;color:var(--ink);position:relative}
  .sheet{position:absolute;top:250px;width:540px;height:700px;background:var(--paper);box-shadow:0 6px 18px rgba(0,0,0,.18)}
  .sheet--front{left:40px}
  .sheet--back{left:620px}
  .photo{position:absolute;display:block}
  .photo--aerial{background:linear-gradient(160deg,#3f6b35 0%,var(--photo-green) 45%,var(--photo-roof) 70%,#c9b99b 100%)}
  .photo--garden{background:linear-gradient(180deg,var(--photo-sky) 0%,#e6dccb 45%,var(--photo-green) 100%)}
  .photo--pool{background:linear-gradient(180deg,#4f7a3f 0%,#6fb9c6 55%,#c2a58a 100%)}
  .photo--interior{background:linear-gradient(180deg,#f1ece3 0%,var(--photo-interior) 60%,#9c7a58 100%)}

  /* front */
  .hero-photo{left:16px;top:16px;width:300px;height:476px}
  .logo-space{position:absolute;left:334px;top:22px;width:188px;height:58px;border:1px solid #555;display:flex;align-items:center;justify-content:center;font-family:"Montserrat",sans-serif;font-weight:600;font-size:22px}
  .headline{position:absolute;left:334px;top:104px;width:192px;font-family:"Oswald",sans-serif;color:var(--ink);line-height:1.02}
  .headline__a{font-size:40px;font-weight:500;letter-spacing:-.5px;display:block}
  .headline__b{font-size:21px;font-weight:400;display:block;margin-top:2px}
  .headline__c{font-size:50px;font-weight:400;display:block}
  .headline__band{position:absolute;left:330px;top:258px;width:200px;height:52px;background:var(--band-dark);color:var(--on-dark);font-family:"Oswald",sans-serif;font-size:27px;display:flex;align-items:center;justify-content:center}
  .stats{position:absolute;left:330px;top:332px;width:200px;height:160px;background:var(--gold);color:var(--on-dark);font-family:"Montserrat",sans-serif;font-size:18px;font-weight:500;list-style:none;padding:28px 0 0 14px}
  .stats li{margin-bottom:14px;display:flex;align-items:center;gap:8px}
  .stats li::before{content:"»";font-size:20px}
  .offer{position:absolute;left:16px;top:505px;width:160px;height:118px;background:var(--gold);color:var(--on-dark);padding:26px 14px 0}
  .offer__label{font-size:15px;padding-bottom:8px;border-bottom:1px solid rgba(255,255,255,.6)}
  .offer__price{font-family:"Oswald",sans-serif;font-size:38px;font-weight:500;margin-top:6px}
  .pool-photo{left:184px;top:505px;width:166px;height:118px}
  .yard-photo{left:358px;top:505px;width:166px;height:118px}

  /* footer shared */
  .contact-bar{position:absolute;left:0;bottom:0;width:100%;height:62px;background:var(--footer);color:var(--on-dark);display:flex;justify-content:space-between;padding:12px 18px 0}
  .contact-bar__who{font-family:"Montserrat",sans-serif;font-size:13px;font-weight:500;letter-spacing:.3px}
  .contact-bar__email{display:flex;align-items:center;gap:5px;font-size:10px;letter-spacing:2px;margin-top:4px}
  .contact-bar__where{font-size:10px;line-height:1.45;width:200px}
  .contact-bar__row{display:flex;gap:5px;align-items:flex-start}
  .contact-bar__phone{font-weight:600;font-size:11px}
  .icon{flex:none;margin-top:2px}

  /* back */
  .aerial-wide{left:16px;top:16px;width:508px;height:165px}
  .side-photo{left:16px;top:190px;width:250px;height:124px}
  .patio-photo{left:274px;top:190px;width:250px;height:124px}
  .features{position:absolute;left:16px;top:324px;width:508px;height:168px;background:var(--gold);color:var(--on-dark);display:grid;grid-template-columns:1fr 1fr;font-size:9.5px;line-height:1.35}
  .features ul{list-style:none;padding:14px 14px 0}
  .features ul + ul{border-left:1px solid rgba(255,255,255,.45)}
  .features li{display:flex;gap:5px;margin-bottom:14px}
  .lanai-photo{left:16px;top:502px;width:250px;height:128px}
  .dining-photo{left:274px;top:502px;width:250px;height:128px}
</style>
</head>
<body>

<section class="sheet sheet--front" aria-label="Flyer front">
  <div class="photo photo--aerial hero-photo" role="img" aria-label="Aerial view of the corner-lot pool home with tiled roof, paver driveway and palms"></div>
  <div class="logo-space">Logo Space</div>
  <h1 class="headline">
    <span class="headline__a">POOL HOME</span>
    <span class="headline__b">ON COVETED CORNER</span>
    <span class="headline__c">LOT WITH</span>
  </h1>
  <div class="headline__band">OVERSIZED YARD</div>
  <ul class="stats">
    <li>Size – 2,307 SF</li>
    <li>3 bedrooms</li>
    <li>2 ½ bathrooms</li>
  </ul>
  <div class="offer">
    <p class="offer__label">Offer Price</p>
    <p class="offer__price">$570,000</p>
  </div>
  <div class="photo photo--pool pool-photo" role="img" aria-label="Screened pool and paver deck"></div>
  <div class="photo photo--garden yard-photo" role="img" aria-label="Front of the home from the left with large lawn"></div>
  <footer class="contact-bar">
    <div>
      <p class="contact-bar__who">Dana Whitlock is the contact person.</p>
      <p class="contact-bar__email"><svg class="icon" width="9" height="7" viewBox="0 0 9 7"><rect x=".5" y=".5" width="8" height="6" fill="none" stroke="#fff"/><path d="M.5 .5 4.5 4 8.5 .5" fill="none" stroke="#fff"/></svg>dana@whitlockhomes.com</p>
    </div>
    <div class="contact-bar__where">
      <p class="contact-bar__row contact-bar__phone"><svg class="icon" width="9" height="9" viewBox="0 0 10 10"><path d="M2 1 4 3 3 4.5Q4.5 6.5 5.5 7L7 6 9 8 7.5 9.5Q2 8 .5 2.5Z" fill="#fff"/></svg>561-555-0142</p>
      <p class="contact-bar__row"><svg class="icon" width="8" height="10" viewBox="0 0 8 10"><path d="M4 10 C1 6 .5 5 .5 3.5a3.5 3.5 0 0 1 7 0C7.5 5 7 6 4 10Z" fill="#fff"/><circle cx="4" cy="3.5" r="1.2" fill="#5b5b5b"/></svg>4817 Heron Lane, Palm Beach Gardens, FL 58127.</p>
    </div>
  </footer>
</section>

<section class="sheet sheet--back" aria-label="Flyer back">
  <div class="photo photo--aerial aerial-wide" role="img" aria-label="Aerial of the neighborhood with the home outlined on its corner lot"></div>
  <div class="photo photo--garden side-photo" role="img" aria-label="Paver walkway along the side entry"></div>
  <div class="photo photo--garden patio-photo" role="img" aria-label="Expanded patio with dining table beside the oversized yard"></div>
  <div class="features">
    <ul>
      <li><span>✓</span><span>This impressive home boasts one of the largest yards in Palm Beach Gardens' most family friendly community, Willowmere.</span></li>
      <li><span>✓</span><span>Enjoy the ultimate Florida lifestyle with a beautiful pool &amp; expanded patio areas - perfect for entertaining.</span></li>
      <li><span>✓</span><span>Upgraded features throughout. Custom wood and ship lap details in all bathrooms and loft.</span></li>
    </ul>
    <ul>
      <li><span>✓</span><span>New dark wood laminate flooring upstairs. New high-efficiency A/C units with smart thermostats.</span></li>
      <li><span>✓</span><span>New pool pump and new heater controlled from your phone! Crown molding throughout.</span></li>
      <li><span>✓</span><span>Walk-in closets.</span></li>
      <li><span>✓</span><span>Quiet &amp; private cul-de-sac.</span></li>
    </ul>
  </div>
  <div class="photo photo--interior lanai-photo" role="img" aria-label="Covered lanai with ceiling fan and french doors"></div>
  <div class="photo photo--interior dining-photo" role="img" aria-label="Dining room with chandelier and pool view"></div>
  <footer class="contact-bar">
    <div>
      <p class="contact-bar__who">Dana Whitlock is the contact person.</p>
      <p class="contact-bar__email"><svg class="icon" width="9" height="7" viewBox="0 0 9 7"><rect x=".5" y=".5" width="8" height="6" fill="none" stroke="#fff"/><path d="M.5 .5 4.5 4 8.5 .5" fill="none" stroke="#fff"/></svg>dana@whitlockhomes.com</p>
    </div>
    <div class="contact-bar__where">
      <p class="contact-bar__row contact-bar__phone"><svg class="icon" width="9" height="9" viewBox="0 0 10 10"><path d="M2 1 4 3 3 4.5Q4.5 6.5 5.5 7L7 6 9 8 7.5 9.5Q2 8 .5 2.5Z" fill="#fff"/></svg>561-555-0142</p>
      <p class="contact-bar__row"><svg class="icon" width="8" height="10" viewBox="0 0 8 10"><path d="M4 10 C1 6 .5 5 .5 3.5a3.5 3.5 0 0 1 7 0C7.5 5 7 6 4 10Z" fill="#fff"/><circle cx="4" cy="3.5" r="1.2" fill="#5b5b5b"/></svg>4817 Heron Lane, Palm Beach Gardens, FL 58127.</p>
    </div>
  </footer>
</section>

</body>
</html>
```